Tabloid Magazine Flyer Class Action Lawsuit

Create a bold, 2-page 8.5" x 11" flyer with the look and feel of a tabloid exposé — loud, sensational, and impossible to ignore. Use bold fonts, dramatic headlines, and high-contrast colors (red, black, white, deep blue). Fill every inch of space — no white space, no subtlety. Use the provided images prominently. Page 1 should grab attention with a shocking headline, impactful image, and strong call to action. Page 2 should stack bold subheadings and explosive bullet points. Emphasize urgency, outrage, and grassroots power. This flyer is meant to rally a community.
Updates

Need to extend because we haven't received a design that meets our needs

Target Market(s)

All instructions and content are in the attached word doc

Industry/Entity Type

Requirements
Must have
• All instructions and content are in the attached word doc
Nice to have
Should not have

```html
<!DOCTYPE html>
<html lang="en">
<head>
<meta charset="utf-8">
<title>Harbor Park Exposed – Flyer</title>
<link href="https://fonts.googleapis.com/css2?family=Anton&family=Oswald:wght@500;700&family=Roboto:wght@400;700;900&display=swap" rel="stylesheet">
<style>
  :root{
    --navy:#1b2f6b;
    --blue:#1f4fa3;
    --red:#d62430;
    --deep-red:#a8141e;
    --ink:#1a1a1a;
    --white:#ffffff;
    --stage:#ffffff;
    --muted:#4a4a4a;
  }
  *{box-sizing:border-box;margin:0;padding:0}
  html,body{width:1200px;height:1191px;overflow:hidden;background:var(--stage)}
  body{position:relative;font-family:"Roboto",Arial,sans-serif;color:var(--ink)}

  .page{position:absolute;width:510px;height:660px;background:var(--white);overflow:hidden;box-shadow:0 6px 22px rgba(0,0,0,.22)}
  .page--front{left:70px;top:160px}
  .page--back{left:620px;top:300px}

  /* FRONT */
  .hero-photo{position:absolute;left:0;top:0;width:100%;height:128px;background:linear-gradient(180deg,#2a3566 0%,#7a4a52 45%,#d88a4a 80%,#e9b06a 100%)}
  .url-pill{position:absolute;left:50%;top:110px;transform:translateX(-50%);background:var(--blue);color:var(--white);font:700 17px "Oswald",sans-serif;padding:4px 22px;border-radius:18px;border:2px solid var(--white);white-space:nowrap}
  .headline{position:absolute;left:0;right:0;top:146px;text-align:center;font-family:"Anton",Impact,sans-serif;line-height:.92;letter-spacing:1px}
  .headline span{display:block}
  .headline .l1{font-size:78px;color:var(--navy)}
  .headline .l2{font-size:86px;color:var(--red)}
  .headline .l3{font-size:72px;color:var(--navy)}
  .shock-band{position:absolute;left:0;right:0;top:378px;background:linear-gradient(90deg,var(--navy),var(--red) 25%,var(--red) 75%,var(--navy));color:var(--white);text-align:center;font:700 19px/1.15 "Oswald",sans-serif;padding:5px 0}
  .rally{position:absolute;left:0;right:0;top:432px;text-align:center}
  .rally h2{font:900 19px "Roboto",sans-serif;color:var(--navy)}
  .rally p{font:400 13px/1.3 "Roboto",sans-serif;color:var(--ink)}
  .rally .join{font:700 19px "Oswald",sans-serif;color:var(--red);margin-top:4px}
  .rally .venue{font:700 19px "Oswald",sans-serif;color:var(--navy)}
  .event-row{display:flex;justify-content:center;gap:26px;margin-top:4px;font:700 13px "Roboto",sans-serif}
  .event-row span,.event-place{display:inline-flex;align-items:center;gap:5px}
  .event-place{font:700 12px "Roboto",sans-serif;margin-top:2px}
  .save{margin-top:5px;font:700 16px/1.15 "Oswald",sans-serif}
  .save .r{color:var(--red);display:block}
  .save .b{color:var(--navy);display:block}
  .lawsuit-band{position:absolute;left:0;right:0;bottom:0;height:78px;background:linear-gradient(90deg,var(--navy),var(--blue));color:var(--white);padding:10px 14px}
  .lawsuit-band h3{font:700 17px "Oswald",sans-serif;display:inline-block;border-bottom:2px solid var(--red)}
  .lawsuit-band p{font:400 8.5px/1.3 "Roboto",sans-serif;width:300px;margin-top:4px}
  .partner-mark{position:absolute;right:14px;bottom:16px;display:flex;align-items:center;gap:6px;font:700 12px "Oswald",sans-serif;color:var(--white)}
  .partner-mark i{display:block;width:22px;height:22px;background:var(--red)}

  /* BACK */
  .crowd-photo{position:absolute;right:0;top:0;width:170px;height:128px;background:linear-gradient(160deg,#3c8ad1,#e87c5a 60%,#c23a3a);border-bottom-left-radius:60px}
  .side-photo{position:absolute;right:18px;width:86px;height:86px;border-radius:50%;border:4px solid var(--blue)}
  .side-photo.p1{top:150px;background:linear-gradient(135deg,#6d4c8a,#d95b5b)}
  .side-photo.p2{top:255px;background:linear-gradient(135deg,#3b7bbf,#8fc1e4);border-color:var(--red)}
  .side-photo.p3{top:360px;background:linear-gradient(135deg,#2d5f9e,#9fb4c8)}
  .side-photo.p4{top:465px;background:linear-gradient(135deg,#5a3a22,#c49b5a);border-color:var(--red)}
  .dossier{position:absolute;left:20px;top:18px;width:360px}
  .dossier h4{font:700 10.5px "Oswald",sans-serif;color:var(--red);margin-top:6px;line-height:1.1}
  .dossier p{font:400 7.6px/1.3 "Roboto",sans-serif;color:var(--ink)}
  .dossier .intro-title{font:700 15px "Oswald",sans-serif;color:var(--red)}
  .dossier .know{font:700 17px "Oswald",sans-serif;color:var(--navy);margin:8px 0 0;padding-bottom:2px;border-bottom:2px solid var(--red);width:280px}
  .closing-band{position:absolute;left:0;right:0;bottom:0;height:86px;background:linear-gradient(90deg,var(--navy),var(--blue));color:var(--white);padding:10px 20px}
  .closing-band .c1{font:700 15px "Oswald",sans-serif;display:block}
  .closing-band .c2{font:700 12px "Oswald",sans-serif;display:block;color:#ffd9db}
  .closing-band .site{font:700 26px "Oswald",sans-serif;display:block;margin-top:2px}
  .badges{position:absolute;right:18px;bottom:18px;display:flex;gap:6px}
  .badges i{display:block;width:24px;height:24px;background:var(--white);border-radius:4px}
  .badges i:last-child{background:var(--red)}
</style>
</head>
<body>

<section class="page page--front">
  <div class="hero-photo" role="img" aria-label="Photo of the seaside amusement park with roller coaster at dusk"></div>
  <div class="url-pill">www.FixHarborPark.com</div>
  <h1 class="headline"><span class="l1">HARBOR</span><span class="l2">PARK</span><span class="l3">EXPOSED</span></h1>
  <div class="shock-band">DISABLED CHILD TRAUMATIZED<br>PUBLIC LAND ABUSED FOR PROFIT</div>
  <div class="rally">
    <h2>Help Our Beach Community Fight Back</h2>
    <p>Harbor park is not private. It is public property<br>Owned by the city, paid for by you.</p>
    <div class="join">Join us &amp; show your support @</div>
    <div class="venue">SEACREST BEACH TOWN COUNCIL MEETING</div>
    <div class="event-row">
      <span><svg width="14" height="14" viewBox="0 0 14 14"><rect x="1" y="2" width="12" height="11" rx="1" fill="#d62430"/><rect x="1" y="5" width="12" height="8" fill="#fff"/><rect x="3" y="7" width="2" height="2" fill="#d62430"/></svg>May 14, 2025</span>
      <span><svg width="14" height="14" viewBox="0 0 14 14"><circle cx="7" cy="7" r="6" fill="none" stroke="#1b2f6b" stroke-width="1.6"/><path d="M7 3.5V7l2.5 1.5" stroke="#1b2f6b" stroke-width="1.6" fill="none"/></svg>6:00 PM</span>
    </div>
    <div class="event-place"><svg width="12" height="14" viewBox="0 0 12 14"><path d="M6 13S1 8 1 5a5 5 0 0 1 10 0c0 3-5 8-5 8z" fill="#d62430"/><circle cx="6" cy="5" r="1.8" fill="#fff"/></svg>Harbor Park Community Room (Above The Arcade)</div>
    <div class="save"><span class="r">HELP OUR COMMUNITY SAVE HARBOR PARK</span><span class="b">HARBOR PARK WAS BUILT FOR FAMILIES — NOT RAVES</span></div>
  </div>
  <div class="lawsuit-band">
    <h3>CLASS ACTION LAWSUIT FORMING NOW!</h3>
    <p>If you or your family were harmed by noise, crowds or illegal events, you may be eligible to join. Share your story and protect your rights.</p>
    <div class="partner-mark"><i></i>RIGHTS ALLIANCE</div>
  </div>
</section>

<section class="page page--back">
  <div class="crowd-photo" role="img" aria-label="Photo of a packed rave crowd on the beach"></div>
  <div class="side-photo p1" role="img" aria-label="Photo of a nighttime rave stage"></div>
  <div class="side-photo p2" role="img" aria-label="Photo of portable toilets lined along the beach"></div>
  <div class="side-photo p3" role="img" aria-label="Photo of a fenced-off park area"></div>
  <div class="side-photo p4" role="img" aria-label="Photo of a judge's gavel"></div>

  <div class="dossier">
    <div class="intro-title">EXPOSED:</div>
    <p>Dana Reyes, CEO of Harbor Park LLC, the leaseholder of Harbor Park, has turned community land into a private profit machine, ignoring permits and putting local families at risk every weekend.</p>
    <div class="know">WHAT THEY DON'T WANT YOU TO KNOW:</div>
    <h4>ILLEGAL RAVES – NO PERMITS</h4>
    <p>Harbor Park hosted over 100 late-night raves without city approval. Police logs, noise complaints and neighbor videos show the events ran with no permits and no safety plan.</p>
    <h4>THE BEACH NO ONE OWNS – IT'S YOURS</h4>
    <p>This park sits on public tidelands held in trust for every resident. Fences, wristbands and VIP zones now lock families out of the shoreline they already paid for.</p>
    <h4>DISABLED CHILD TRAUMATIZED BY RAVE NOISE</h4>
    <p>A disabled child living next door suffered repeated panic attacks from bass levels past midnight. Requests for quiet hours and basic accommodation were ignored again and again.</p>
    <h4>EXPOSED: IS HARBOR PARK RUNNING A SELF-DEALING SCHEME?</h4>
    <p>Records show event contracts flowing to companies tied to park insiders. Public revenue that should fund upkeep appears to be steered toward private partners.</p>
    <h4>DOCUMENTED NUISANCE AND ENVIRONMENTAL DISASTER</h4>
    <p>Trash, broken glass and overflowing toilets spill onto the sand after every event. Storm drains carry the waste straight into the bay while cleanup is delayed.</p>
    <h4>EXPOSED: HARBOR PARK'S ILLEGAL SIGNS MISLEAD THE PUBLIC</h4>
    <p>Posted signs claim the boardwalk and lawn are private property. They are not. Residents have been told to leave land they have every right to use.</p>
    <h4>HARBOR PARK: AN ACCIDENT WAITING TO HAPPEN</h4>
    <p>Overcrowded walkways, blocked exits and aging rides create real danger. One bad night is all it takes. We are asking the city to act before someone is hurt.</p>
  </div>

  <div class="closing-band">
    <span class="c1">HELP OUR COMMUNITY SAVE HARBOR PARK</span>
    <span class="c2">HARBOR PARK WAS BUILT FOR FAMILIES — NOT RAVES</span>
    <span class="site">www.FixHarborPark.com</span>
    <div class="badges"><i></i><i></i></div>
  </div>
</section>

</body>
</html>
```